Lumo Organic Baby Wipes for retail sales into supermarkets

Design a new Organic Baby Wipes Pack that has a similar feel and details to the attachments under the Brand Name LUMO Organics. Please keep all writing in English and highlight the following info on the Pack. - 80 Pack, 100% Biodegradable,
Aloe Vera, Chamomile,Natural Vitamin E to soothe baby's skin.
Hypo Allergenic, pH Balanced for baby's skin.
Fragrance Free, Alcohol Free, Chlorine Free, Parabens Free.

Target Market(s)

Mums looking for a Organic Baby Wipe

Industry/Entity Type

Baby

Font styles to use
Sans Serif

Colors
9bcb3c
abd036
cadf82
ffffff

Requirements
Must have
• Lumo Organics, White Base, majority green writing with different shades, touches of Brown to represent Bamboo Wipes.
• Please make ORGANIC writing very big.
Nice to have
• Natural Organic feel going to use matt packaging.
Should not have
• Cluttered too much information

```html
<!DOCTYPE html>
<html lang="en">
<head>
<meta charset="utf-8">
<title>Lumo Organics – Organic Baby Wipes Pack Front</title>
<link rel="stylesheet" href="https://fonts.googleapis.com/css2?family=Cabin:wght@500;600;700&family=Oswald:wght@300;400&display=swap">
<style>
  :root{
    --bg:#ffffff;
    --pack:#ffffff;
    --seal:#eceee8;
    --seal-line:#d5d8d0;
    --photo-deep:#abd036;
    --photo-mid:#cadf82;
    --brand-purple:#8b1b7f;
    --bamboo-brown:#8a6a3f;
    --green-bold:#5ea82c;
    --green-soft:#9bcb3c;
    --green-badge:#9bcb3c;
    --green-dark:#3f8a1e;
    --white:#ffffff;
  }
  *{box-sizing:border-box;margin:0;padding:0}
  html,body{width:1200px;height:755px;overflow:hidden;background:var(--bg)}
  .canvas{position:relative;width:1200px;height:755px}
  .pack{
    position:absolute;left:68px;top:120px;width:1072px;height:464px;
    background:var(--pack);overflow:hidden;
    box-shadow:0 6px 18px rgba(0,0,0,.08);
  }
  .seal{position:absolute;top:0;width:44px;height:100%;
    background:repeating-linear-gradient(90deg,var(--seal) 0 5px,var(--seal-line) 5px 7px);}
  .seal--left{left:0}
  .seal--right{right:0}
  .hero-photo{
    position:absolute;left:44px;top:0;width:700px;height:464px;
    background:
      radial-gradient(ellipse 240px 280px at 230px 220px,var(--photo-mid) 0%,transparent 70%),
      linear-gradient(90deg,#b6d56a 0%,var(--photo-mid) 55%,rgba(202,223,130,.5) 78%,rgba(255,255,255,0) 100%);
  }
  .opening-window{position:absolute;left:378px;top:132px}
  .brand{
    position:absolute;left:718px;top:48px;
    font-family:"Cabin",sans-serif;font-weight:700;font-size:42px;line-height:1;
    color:var(--brand-purple);white-space:nowrap;
  }
  .product-line{
    position:absolute;left:764px;top:110px;
    font-family:"Cabin",sans-serif;font-weight:600;font-size:16px;letter-spacing:3px;
    color:var(--bamboo-brown);
  }
  .variant{
    position:absolute;left:762px;top:140px;
    font-family:"Cabin",sans-serif;font-weight:700;color:var(--green-bold);
  }
  .variant__organic{display:block;font-size:50px;line-height:50px}
  .variant__wipes{display:block;font-size:26px;line-height:28px;color:var(--green-soft)}
  .benefits{
    position:absolute;left:764px;top:232px;list-style:none;
    font-family:"Oswald",sans-serif;font-weight:300;font-size:13px;line-height:20px;
    color:var(--green-dark);white-space:nowrap;
  }
  .benefits li::before{content:"";display:inline-block;width:6px;height:6px;border-radius:50%;
    background:var(--bamboo-brown);margin-right:7px;vertical-align:2px}
  .count-badge{
    position:absolute;left:828px;top:352px;width:66px;height:74px;border-radius:12px;
    background:var(--green-badge);color:var(--white);text-align:center;
    font-family:"Oswald",sans-serif;
  }
  .count-badge__number{display:block;font-weight:400;font-size:28px;line-height:28px;margin-top:12px}
  .count-badge__unit{display:block;font-weight:300;font-size:15px;line-height:18px}
  .claim-band{
    position:absolute;left:327px;top:378px;width:414px;height:48px;
    background:linear-gradient(90deg,var(--bamboo-brown) 0%,var(--green-dark) 35%,var(--green-soft) 100%);
    color:var(--white);font-family:"Cabin",sans-serif;font-weight:500;font-size:17px;
    letter-spacing:4px;line-height:48px;padding-left:34px;white-space:nowrap;
  }
</style>
</head>
<body>
<div class="canvas">
  <section class="pack" aria-label="Lumo Organics organic baby wipes pack front">
    <div class="hero-photo" role="img" aria-label="Photo of a smiling baby lying on soft bedding in green tones"></div>

    <svg class="opening-window" width="358" height="204" viewBox="0 0 358 204" aria-hidden="true">
      <path d="M16 0 H300 A16 16 0 0 1 316 16 V50 C342 58 358 78 358 102 C358 126 342 146 316 154 V188 A16 16 0 0 1 300 204 H16 A16 16 0 0 1 0 188 V16 A16 16 0 0 1 16 0 Z"
            fill="#ffffff" fill-opacity="0.45" stroke="#ffffff" stroke-opacity="0.6"/>
    </svg>

    <div class="seal seal--left" aria-hidden="true"></div>
    <div class="seal seal--right" aria-hidden="true"></div>

    <h1 class="brand">Lumo Organics</h1>
    <p class="product-line">BABY WIPES</p>
    <h2 class="variant">
      <span class="variant__organic">ORGANIC</span>
      <span class="variant__wipes">BAMBOO WIPES</span>
    </h2>
    <ul class="benefits">
      <li>ALOE VERA, CHAMOMILE &amp; NATURAL VITAMIN E</li>
      <li>HYPO ALLERGENIC &amp; PH BALANCED</li>
      <li>FRAGRANCE, ALCOHOL, CHLORINE &amp; PARABEN FREE</li>
      <li>GENTLY SOOTHES BABY'S SKIN</li>
    </ul>
    <div class="count-badge">
      <span class="count-badge__number">80</span>
      <span class="count-badge__unit">PACK</span>
    </div>
    <div class="claim-band">100% BIODEGRADABLE</div>
  </section>
</div>
</body>
</html>
```